Email Banner for Technology Company

We need a new email banner. The purpose of the email banner is to make us look more professional as a business and keep all communications with clients uniform. The previous designs which we have included below have now become outdated as our brand has developed and we need the new banner to become more aligned and modern.

We are a marketing organization that specialises in lead generation, email newsletters are sent to prospects on a regular basis. Therefore, it is important that we have an aesthetically pleasing banner as this is the first real impression prospects have our business. First impressions matter.

We are looking for a new email banner design as the current design is now outdated and does not reflect who we are as a business.

The new banners are required for launch at the start of Q2.

There is future work in the pipeline for the winning design. We have multiple industry sites that will require the new design as well as creating each of these in multiple languages.

The design must include the Zevomarkly wording the tagline 'The Ultimate Research Library for Technology Pro's.
It needs to be creative and fun but still remain professional, sticking with the colour theme that already exists.

Requirements
Must have
• The design must include the Zevomarkly wording the tagline 'The Ultimate Research Library for Technology Pro's.

```html
<!DOCTYPE html>
<html lang="en">
<head>
<meta charset="utf-8">
<title>Zevomarkly Email Banner Concepts</title>
<link href="https://fonts.googleapis.com/css2?family=Poppins:wght@600;700&family=PT+Sans&display=swap" rel="stylesheet">
<style>
  :root {
    --sheet-grey: #d3d3d3;
    --white: #ffffff;
    --brand-blue: #2b8ed3;
    --brand-blue-deep: #2456a8;
    --navy: #1b1d55;
    --navy-dark: #121a30;
    --navy-band: #243a82;
    --midnight: #0e1638;
    --ember: #6a2238;
    --note-ink: #111111;
  }
  * { box-sizing: border-box; margin: 0; padding: 0; }
  html, body {
    width: 1200px; height: 760px; overflow: hidden;
    background: var(--sheet-grey);
  }
  .sheet { position: relative; width: 1200px; height: 760px; }
  .banner {
    position: absolute; left: 43px; width: 1113px; height: 133px;
    overflow: hidden;
    font-family: "Poppins", sans-serif;
  }
  .banner--split { top: 45px; background: var(--white); }
  .banner--waves { top: 203px; background: var(--navy-band); }
  .banner--clouds { top: 361px; background: var(--navy); }
  .banner--circuit { top: 519px; background: var(--midnight); }

  .banner__art { position: absolute; inset: 0; width: 100%; height: 100%; display: block; }

  .logo-name {
    position: absolute; top: 50%; transform: translate(-50%, -50%);
    font-weight: 600; font-size: 14px; color: var(--white); white-space: nowrap;
  }
  .tagline {
    position: absolute; top: 50%; transform: translate(-50%, -50%);
    font-weight: 700; font-size: 22.5px; white-space: nowrap;
  }
  .tagline--blue { color: var(--brand-blue); }
  .tagline--white { color: var(--white); }

  .cta {
    position: absolute; display: flex; align-items: center; justify-content: center;
    font-weight: 600; font-size: 13.5px; color: var(--white); text-transform: uppercase;
  }
  .cta--tab {
    right: 0; top: 0; width: 148px; height: 33px;
    background: var(--navy-dark); border-bottom-left-radius: 14px;
  }
  .cta--pill {
    height: 53px; border-radius: 27px;
    background: var(--navy); border: 1px solid var(--white);
  }

  .brief-note {
    position: absolute; left: 47px; top: 693px;
    font-family: "PT Sans", sans-serif; font-size: 28.5px; color: var(--note-ink);
    white-space: nowrap;
  }
</style>
</head>
<body>
<main class="sheet">

  <!-- Concept 1: split panel -->
  <section class="banner banner--split">
    <svg class="banner__art" viewBox="0 0 1113 133" aria-hidden="true">
      <defs>
        <linearGradient id="splitBlue" x1="0" x2="1">
          <stop offset="0" stop-color="#2350a6"/>
          <stop offset="1" stop-color="#2996d4"/>
        </linearGradient>
        <linearGradient id="splitSheen" x1="0" x2="1">
          <stop offset="0" stop-color="#d9d9dc"/>
          <stop offset="1" stop-color="#ffffff"/>
        </linearGradient>
      </defs>
      <polygon points="0,0 389,0 314,133 0,133" fill="url(#splitSheen)"/>
      <polygon points="0,0 318,0 241,133 0,133" fill="var(--navy-dark)"/>
      <polygon points="300,0 306,0 229,133 223,133" fill="#c9ccd3"/>
      <polygon points="305,0 338,24 322,24" fill="#2d4fb0"/>
      <polygon points="0,24 338,24 284,117 0,117" fill="url(#splitBlue)"/>
    </svg>
    <span class="logo-name" style="left:139px;">Zevomarkly Logo</span>
    <p class="tagline tagline--blue" style="left:716px;">The Ultimate Research Library for Technology Pro's</p>
    <a class="cta cta--tab">Click here</a>
  </section>

  <!-- Concept 2: arrow ribbon -->
  <section class="banner banner--waves">
    <svg class="banner__art" viewBox="0 0 1113 133" role="img" aria-label="Flowing blue dot-wave pattern background">
      <defs>
        <radialGradient id="waveGlow" cx="0.5" cy="0.6" r="0.8">
          <stop offset="0" stop-color="#2b5bb5"/>
          <stop offset="1" stop-color="#233579"/>
        </radialGradient>
      </defs>
      <rect width="1113" height="133" fill="url(#waveGlow)"/>
    </svg>
    <svg class="banner__art" viewBox="0 0 1113 133" aria-hidden="true">
      <polygon points="271,44 920,44 943,70 920,96 271,96" fill="var(--white)"/>
      <polygon points="943,44 958,44 981,70 958,96 943,96 966,70" fill="var(--white)"/>
      <polygon points="976,44 991,44 1014,70 991,96 976,96 999,70" fill="var(--white)"/>
    </svg>
    <span class="logo-name" style="left:139px;">Zevomarkly Logo</span>
    <p class="tagline tagline--blue" style="left:295px; transform:translateY(-50%);">The Ultimate Research Library for Technology Pro's</p>
    <a class="cta cta--pill" style="left:987px; top:43px; width:114px;">Click here</a>
  </section>

  <!-- Concept 3: cloud sky -->
  <section class="banner banner--clouds">
    <svg class="banner__art" viewBox="0 0 1113 133" role="img" aria-label="Illustrated blue cloud shapes drifting across a navy sky">
      <defs>
        <linearGradient id="cloudSky" x1="0" x2="1">
          <stop offset="0" stop-color="#1d1d58"/>
          <stop offset="0.45" stop-color="#22306e"/>
          <stop offset="0.8" stop-color="#243778"/>
          <stop offset="1" stop-color="#1d1d58"/>
        </linearGradient>
      </defs>
      <rect width="1113" height="133" fill="url(#cloudSky)"/>
    </svg>
    <span class="logo-name" style="left:111px;">Zevomarkly Logo</span>
    <p class="tagline tagline--white" style="left:564px;">The Ultimate Research Library for Technology Pro's</p>
    <a class="cta cta--pill" style="left:945px; top:46px; width:145px;">Click here</a>
  </section>

  <!-- Concept 4: circuit glow -->
  <section class="banner banner--circuit">
    <svg class="banner__art" viewBox="0 0 1113 133" role="img" aria-label="Red glowing circuit line pattern over dark navy">
      <defs>
        <radialGradient id="circuitGlow" cx="0.58" cy="0.75" r="0.6">
          <stop offset="0" stop-color="#6a2238"/>
          <stop offset="0.6" stop-color="#2a1a45"/>
          <stop offset="1" stop-color="#0e1638"/>
        </radialGradient>
      </defs>
      <rect width="1113" height="133" fill="url(#circuitGlow)"/>
    </svg>
    <span class="logo-name" style="left:111px;">Zevomarkly Logo</span>
    <p class="tagline tagline--white" style="left:564px;">The Ultimate Research Library for Technology Pro's</p>
    <a class="cta cta--pill" style="left:945px; top:46px; width:145px;">Click here</a>
  </section>

  <p class="brief-note">Please provide me the logo and the brand colors to send the exact design :) Thanks</p>
</main>
</body>
</html>
```